for an application under development,
this application will be used for the management of files in a company for several remote collaborators.
it is like an internal messaging system where files will be opened for such and such a person or group of people.

Target Market(s)

business

Number of Pages Required

5+ page

Requirements
Nice to have
• a visual with the view of a connection between computer and / or smart phones
the name of my application; "LumaKTrovenar"

```html
<!DOCTYPE html>
<html lang="en">
<head>
<meta charset="utf-8">
<title>LumaKTrovenar</title>
<link rel="stylesheet" href="https://fonts.googleapis.com/css2?family=Lato:wght@400;700;900&display=swap">
<style>
:root{
  --navy:#1b1f5e;
  --hero-a:#1a2470;
  --hero-b:#2d55b5;
  --card-a:#1e2366;
  --card-b:#1f6ca6;
  --orange:#f46a1c;
  --grey:#f1f1f1;
  --text:#3a3a3a;
  --dark:#242424;
  --white:#ffffff;
}
*{margin:0;padding:0;box-sizing:border-box}
html,body{width:1200px;height:4500px;overflow:hidden}
body{position:relative;background:var(--white);font-family:"Lato",sans-serif;color:var(--text)}
.abs{position:absolute}
.backdrop{position:absolute;left:0;top:0}
.brand{display:flex;align-items:center;gap:12px;color:var(--white);font-weight:700;font-size:25px}
.brand-mark{width:30px;height:30px;background:var(--orange);border-radius:4px}
.nav{top:70px;left:373px;display:flex;align-items:center;height:38px}
.nav a{color:var(--white);text-decoration:none;font-size:12.5px;font-weight:700;letter-spacing:.3px;margin-right:40px;position:relative;line-height:38px}
.nav a.active::after{content:"";position:absolute;left:-10px;right:-10px;bottom:-2px;height:3px;background:var(--white)}
.btn{display:inline-flex;align-items:center;justify-content:center;background:var(--orange);color:var(--white);font-size:15px;font-weight:700;text-transform:uppercase;text-decoration:none;letter-spacing:.3px}
.btn.dark{background:#2b2b2b}
.hero-title{top:170px;left:0;width:1200px;text-align:center;color:var(--white);font-weight:900;font-size:41px;line-height:50px}
.placeholder{position:absolute}
.section-title{left:0;width:1200px;text-align:center;color:var(--navy);font-weight:900;font-size:31px;text-transform:uppercase}
.lead{left:165px;width:870px;text-align:center;font-size:15px;line-height:26px}
.card{width:331px;height:290px;background:linear-gradient(180deg,var(--card-a),var(--card-b));color:var(--white);text-align:center;padding-top:36px}
.card h3{font-size:25px;font-weight:700;margin-top:18px}
.card p{font-size:13.5px;line-height:26px;margin:10px 28px 0}
.card svg{display:block;margin:0 auto}
.feature-title{left:75px;top:1960px;color:var(--navy);font-weight:900;font-size:31px;line-height:44px;text-transform:uppercase}
.feature-text{left:75px;top:2066px;width:480px;font-size:15px;line-height:29.5px}
.quote-title{top:2560px;left:0;width:1200px;text-align:center;color:var(--white);font-weight:900;font-size:29px}
.photo{border:4px solid var(--white)}
.quote-text{left:676px;top:2752px;width:420px;color:var(--white);font-size:18px;line-height:36px}
.quote-name{left:678px;top:2908px;color:var(--white);font-size:15px;font-weight:900}
.dots{left:678px;top:2973px;display:flex;gap:11px}
.dots span{width:13px;height:13px;border-radius:50%;background:var(--white)}
.dots span.on{background:var(--orange)}
.post-title{color:var(--navy);font-weight:700;font-size:25px;line-height:32px}
.post-text{font-size:15px;line-height:31px;width:515px}
.footer-head{color:var(--white);font-weight:700;font-size:16px;top:4270px}
.footer-list{top:4301px;list-style:none;color:var(--white);font-size:13px;line-height:28px}
.footer-small{color:var(--white);font-size:12px;line-height:22px}
.signup{left:884px;top:4306px;display:flex}
.signup span{width:199px;height:37px;background:var(--white);color:#555;font-size:13px;line-height:37px;padding-left:12px}
.signup b{width:44px;height:37px;background:var(--orange);color:var(--white);font-size:15px;line-height:37px;text-align:center}
.social{left:75px;top:4428px;display:flex;gap:16px}
.social span{width:22px;height:22px;border-radius:50%;background:var(--white)}
</style>
</head>
<body>

<svg class="backdrop" width="1200" height="4500" viewBox="0 0 1200 4500" aria-hidden="true">
  <defs>
    <radialGradient id="heroFill" cx="0.5" cy="0.45" r="0.7">
      <stop offset="0" stop-color="#2f5cbd"/>
      <stop offset="1" stop-color="#1a2470"/>
    </radialGradient>
    <linearGradient id="quoteFill" x1="0" y1="0" x2="0" y2="1">
      <stop offset="0" stop-color="#1d2264"/>
      <stop offset="1" stop-color="#1f72ab"/>
    </linearGradient>
  </defs>
  <path d="M0 0H1200V735C1080 700 950 670 820 690C650 715 500 730 380 715C220 690 90 640 0 520Z" fill="url(#heroFill)"/>
  <path d="M0 1040C150 1100 300 1150 600 1160C900 1170 1100 1190 1200 1240V1890C1000 1820 700 1780 400 1800C200 1810 80 1760 0 1740Z" fill="var(--grey)"/>
  <path d="M1200 2440C1000 2420 700 2420 500 2450C250 2490 90 2600 70 2830C60 3000 150 3150 400 3200C700 3250 1000 3230 1200 3258Z" fill="url(#quoteFill)"/>
  <path d="M0 4220C300 4160 800 4140 1200 4230V4500H0Z" fill="var(--dark)"/>
</svg>

<header>
  <div class="abs brand" style="left:75px;top:70px;height:38px"><span class="brand-mark"></span>LumaKTrovenar</div>
  <nav class="abs nav">
    <a class="active" href="#">HOME</a>
    <a href="#">ABOUT US</a>
    <a href="#">SERVICES</a>
    <a href="#">FEATURES</a>
    <a href="#">BLOG</a>
    <a href="#">CONTACT US</a>
    <a class="btn" href="#" style="margin:0;width:133px;height:38px;font-size:12.5px">REQUEST DEMO</a>
  </nav>
  <h1 class="abs hero-title">A visual with the view of a connection between<br>computer and / or smart phones.</h1>
  <div class="placeholder" role="img" aria-label="Illustration of a hand-held smartphone and a desktop monitor exchanging documents" style="left:250px;top:305px;width:745px;height:410px;background:linear-gradient(90deg,rgba(255,255,255,.14),rgba(255,255,255,.22));border-radius:8px"></div>
</header>

<section>
  <h2 class="abs section-title" style="top:826px">Welcome to LumaKTrovenar</h2>
  <p class="abs lead" style="top:887px">Lorem ipsum dolor sit amet, consectetur adipiscing elit. Curabitur egestas felis libero, ut tristique est maximus id. Nulla tincidunt felis efficitur, interdum mi eu, auctor orci. Fusce tincidunt commodo velit in porttitor. Donec dapibus, lacus quis molestie lobortis, mi elit luctus nisi, a maximus est ex vel lacus.</p>
  <p class="abs lead" style="top:978px">Lorem ipsum dolor sit amet, consectetur adipiscing elit. Curabitur egestas felis libero, ut tristique est maximus id. Nulla tincidunt felis efficitur, interdum mi eu, auctor orci.</p>
  <a class="abs btn" href="#" style="left:517px;top:1071px;width:164px;height:50px">Read More</a>
</section>

<section>
  <h2 class="abs section-title" style="top:1298px">Our Services</h2>
  <p class="abs lead" style="top:1357px">Lorem ipsum dolor sit amet, consectetur adipiscing elit. Curabitur egestas felis libero, ut tristique est maximus id. Nulla tincidunt felis efficitur, interdum mi eu, auctor orci.</p>

  <div class="abs card" style="left:75px;top:1453px">
    <svg width="80" height="74" viewBox="0 0 80 74" fill="none" stroke="#fff" stroke-width="2"><path d="M24 4H62L74 16V66H24Z"/><path d="M62 4V16H74"/><path d="M34 28H64M34 38H64M34 48H64M34 58H56"/><circle cx="20" cy="54" r="9"/><circle cx="20" cy="54" r="15" stroke-dasharray="5 4"/></svg>
    <h3>Nunc Sit Amet</h3>
    <p>Lorem ipsum dolor sit amet, consectetur adipiscing elit. Curabitur egestas felis libero, ut tristique es..</p>
  </div>
  <div class="abs card" style="left:435px;top:1453px">
    <svg width="96" height="74" viewBox="0 0 96 74" fill="none" stroke="#fff" stroke-width="2"><rect x="4" y="28" width="50" height="34"/><path d="M22 62V70H36V62M16 70H42"/><rect x="62" y="4" width="30" height="46" rx="3"/><rect x="40" y="14" width="18" height="26" rx="2"/><path d="M54 28H62"/></svg>
    <h3>Vitae Tempus</h3>
    <p>Lorem ipsum dolor sit amet, consectetur adipiscing elit. Curabitur egestas felis libero, ut tristique es..</p>
  </div>
  <div class="abs card" style="left:795px;top:1453px">
    <div role="img" aria-label="Team icon" style="width:90px;height:74px;margin:0 auto;border:2px solid #fff;border-radius:10px;opacity:.85"></div>
    <h3>Feugiat Tincidunt</h3>
    <p>Lorem ipsum dolor sit amet, consectetur adipiscing elit. Curabitur egestas felis libero, ut tristique es..</p>
  </div>
</section>

<section>
  <h2 class="abs feature-title">Pellentesque non tellus<br>nisl augue dapibus</h2>
  <p class="abs feature-text">Lorem ipsum dolor sit amet, consectetur adipiscing elit. Curabitur egestas felis libero, ut tristique est maximus ulla tincidunt felis efficitur, interdum mi eu, auctor orci usce tincidunt commodo velit in porttitor. Donec dapibus, lacus quis molestie lobortis, mi elit luctus nisi, a maximus est ex vel lacus.</p>
  <a class="abs btn" href="#" style="left:75px;top:2268px;width:166px;height:52px">Request Demo</a>
  <a class="abs btn dark" href="#" style="left:253px;top:2268px;width:166px;height:52px">Watch Video</a>
  <div class="placeholder" role="img" aria-label="Laptop showing the application dashboard with charts and file lists" style="left:605px;top:1962px;width:520px;height:378px;background:linear-gradient(180deg,#2a2d3a,#c9ccd4);border-radius:14px 14px 4px 4px"></div>
</section>

<section>
  <h2 class="abs quote-title">WHAT OUR CLEINT SAYS..</h2>
  <div class="placeholder photo" role="img" aria-label="Portrait of a client" style="left:229px;top:2655px;width:165px;height:167px;background:linear-gradient(180deg,#d8d8d8,#9a8a80)"></div>
  <div class="placeholder" role="img" aria-label="Portrait of a client" style="left:419px;top:2746px;width:165px;height:168px;background:linear-gradient(180deg,#e4e4e4,#b8a196)"></div>
  <div class="placeholder" role="img" aria-label="Portrait of a client" style="left:229px;top:2856px;width:165px;height:168px;background:linear-gradient(180deg,#d4d6da,#4a4f5c)"></div>
  <svg class="abs" style="left:628px;top:2680px" width="64" height="46" viewBox="0 0 64 46" fill="#5a7fc6"><path d="M26 4C12 8 2 18 2 32a12 12 0 1 0 14-12C18 14 22 10 28 8ZM60 4C46 8 36 18 36 32a12 12 0 1 0 14-12C52 14 56 10 62 8Z"/></svg>
  <p class="abs quote-text">Lorem ipsum dolor sit amet, consectetur adipiscing elit. Curabitur egestas felis libero, ut tristique est maximus id. Nulla tincidunt felis efficitur, interdum mi eu..</p>
  <div class="abs quote-name">NAME HEADING</div>
  <div class="abs dots"><span class="on"></span><span></span><span></span><span></span></div>
  <svg class="abs" style="left:1068px;top:2922px" width="64" height="46" viewBox="0 0 64 46" fill="#5a7fc6"><path d="M38 42C52 38 62 28 62 14a12 12 0 1 0-14 12C46 32 42 36 36 38ZM4 42C18 38 28 28 28 14a12 12 0 1 0-14 12C12 32 8 36 2 38Z"/></svg>
</section>

<section>
  <h2 class="abs section-title" style="top:3332px">Recent Blog Post</h2>
  <p class="abs lead" style="top:3392px">Lorem ipsum dolor sit amet, consectetur adipiscing elit. Curabitur egestas felis libero, ut tristique est maximus id. Nulla tincidunt felis efficitur, interdum mi eu, auctor orci.</p>

  <div class="placeholder" role="img" aria-label="Photo of hands using a smartphone with digital interface graphics" style="left:75px;top:3489px;width:512px;height:267px;background:linear-gradient(135deg,#8a5a34,#2e2a28)"></div>
  <h3 class="abs post-title" style="left:75px;top:3780px">Lorem ipsum dolor sit amet, adipiscing elit<br>sed convallis sagittis</h3>
  <p class="abs post-text" style="left:75px;top:3851px">Curabitur egestas felis libero, ut tristique est maximus id incidunt felis efficitur, interdum mi eu, auctor orci. Fusce tincidunt commodo velit in porttitor. Donec dapibus, lacus quis molestie lobortis, mi elit luctus nisi, a maximus est ex vel lacus.</p>
  <a class="abs btn" href="#" style="left:75px;top:4004px;width:166px;height:51px">Read More</a>

  <div class="placeholder" role="img" aria-label="Illustration of file types moving from a phone to a laptop" style="left:615px;top:3489px;width:512px;height:267px;background:linear-gradient(135deg,#e8452a,#d83a22)"></div>
  <h3 class="abs post-title" style="left:614px;top:3780px">Lorem ipsum dolor sit amet, adipiscing elit<br>sed convallis sagittis</h3>
  <p class="abs post-text" style="left:614px;top:3851px">Curabitur egestas felis libero, ut tristique est maximus id incidunt felis efficitur, interdum mi eu, auctor orci. Fusce tincidunt commodo velit in porttitor. Donec dapibus, lacus quis molestie lobortis, mi elit luctus nisi, a maximus est ex vel lacus.</p>
  <a class="abs btn" href="#" style="left:614px;top:4004px;width:166px;height:51px">Read More</a>
</section>

<footer>
  <div class="abs brand" style="left:75px;top:4314px;height:38px"><span class="brand-mark"></span>LumaKTrovenar</div>
  <p class="abs footer-small" style="left:75px;top:4372px">Copyright © 2019. Company Name.<br>All Right Reserved</p>
  <div class="abs social" role="img" aria-label="Social links"><span></span><span></span><span></span><span></span><span></span></div>

  <div class="abs footer-head" style="left:442px">QUICK LINKS</div>
  <ul class="abs footer-list" style="left:442px"><li>Home</li><li>About Us</li><li>Services</li><li>Features</li><li>Blog</li><li>Contact Us</li></ul>

  <div class="abs footer-head" style="left:655px">RESOURCES</div>
  <ul class="abs footer-list" style="left:655px"><li>Donec et suscipit</li><li>Enim at malesuada orc</li><li>Nam purus</li><li>Nulla convallis</li><li>Nulla et volutpat</li></ul>

  <div class="abs footer-head" style="left:884px">EMAIL SIGN UP</div>
  <div class="abs signup"><span>Enter Email Address</span><b>GO</b></div>
</footer>

</body>
</html>
```